Frameless shower doors web site

Build a web site for information and display past projects. Contact information, type of work done. Customer Reviews. The design purpose is to generate phone calls and email inquirers. Domain name is Southernshowerdoors.comEmail is Brightvalebaths@mailbox-demo.com Profile We Love What We Do!Brightvale Bath Panels & Glass LLC. is committed to excellence in every aspect of our business. We hold a standard of integrity bound by fairness, honesty, and personal responsibility. Our distinction is the quality of service and attention to detail we bring to each project. Above all, we listen to our clients input to provide several design options available from designer glass to hardware. We also service and repair existing shower and tub enclosure. Installation of customer purchased enclosure are available by appointment. and address any concerns.

Target Market(s)

25 to 55 residential customers

Number of Pages Required

4 page

Font styles to use
Sans Serif

Colors

Designer to choose colors to be used in the design.

Requirements
Nice to have
• Looking to drive phone calls for estimating shower projects
Should not have
• Lot of prescriptive words, Clutter

```html
<!DOCTYPE html>
<html lang="en">
<head>
<meta charset="utf-8">
<title>Brightvale Bath Panels &amp; Glass</title>
<link href="https://fonts.googleapis.com/css2?family=Montserrat:wght@300;400;500;600;700&family=Open+Sans:wght@400;600&display=swap" rel="stylesheet">
<style>
:root{
  --navy:#1f3b7a;
  --navy-dark:#18306a;
  --green:#6cbf1e;
  --ink:#1d2b4f;
  --text:#555a63;
  --muted:#8a8f97;
  --light:#f3f4f6;
  --charcoal:#2c3037;
  --footer:#24272d;
  --field:#4a4e55;
  --white:#ffffff;
}
*{margin:0;padding:0;box-sizing:border-box}
html,body{width:1200px;height:3854px;overflow:hidden}
body{position:relative;background:var(--white);font-family:"Open Sans",Arial,sans-serif;color:var(--text)}
.abs{position:absolute}
.head{font-family:"Montserrat",Arial,sans-serif}
.btn{position:absolute;display:flex;align-items:center;justify-content:center;border-radius:40px;font-family:"Montserrat",Arial,sans-serif;font-weight:600;color:var(--white)}
.btn-green{background:var(--green)}
.btn-navy{background:var(--navy)}
.photo{position:absolute}

/* header */
.brand{left:36px;top:36px;display:flex;align-items:center;gap:12px}
.brand-mark{width:22px;height:22px;background:var(--navy);border-radius:50%}
.brand-name{font-family:"Montserrat",Arial,sans-serif;font-weight:700;font-size:22px;color:var(--navy);line-height:1}
.nav{left:346px;top:60px;display:flex;gap:38px;font-family:"Montserrat",Arial,sans-serif;font-size:14px;font-weight:500;color:var(--ink)}
.nav .active{color:#2a7fd4}
.nav-phone{left:798px;top:60px;font-family:"Montserrat",Arial,sans-serif;font-size:14px;font-weight:600;color:var(--green)}
.nav-quote{left:975px;top:50px;width:188px;height:38px;font-size:13px}

/* hero */
.hero{left:0;top:0;width:1200px;height:604px;background:linear-gradient(120deg,#f1efec 0%,#d9d6d1 40%,#b9b5ae 75%,#8d8a84 100%)}
.hero-title{left:0;top:230px;width:1200px;text-align:center;font-family:"Montserrat",Arial,sans-serif;font-weight:400;font-size:47px;color:var(--navy)}
.hero-sub{left:0;top:292px;width:1200px;text-align:center;font-family:"Montserrat",Arial,sans-serif;font-weight:600;font-size:30px;color:var(--navy)}
.hero-call{left:456px;top:362px;width:288px;height:48px;font-size:18px;box-shadow:0 0 0 6px rgba(108,191,30,.3)}

/* service tabs */
.tab{position:absolute;top:604px;width:300px;height:296px;overflow:hidden}
.tab-label{position:absolute;left:0;top:0;width:100%;height:54px;background:var(--charcoal);color:var(--white);font-family:"Montserrat",Arial,sans-serif;font-weight:500;font-size:17px;display:flex;align-items:center;padding-left:24px}
.tab-label::before{content:"";position:absolute;left:0;top:0;border-top:26px solid var(--green);border-right:26px solid transparent}
.tab-active .tab-label{background:var(--green);justify-content:center;padding-left:0}
.tab-active .tab-label::before{display:none}
.tab-img{position:absolute;left:0;top:54px;width:100%;height:242px}
.tab-overlay{position:absolute;left:0;top:54px;width:100%;height:242px;background:rgba(40,44,50,.88);padding:26px 32px;color:#e6e8ea;font-size:14px;line-height:19px;text-align:center}
.tab-more{display:block;margin:14px auto 0;color:var(--green);font-size:13px;border-bottom:1px solid var(--green);width:40px}
.estimate{left:900px;top:604px;width:300px;height:296px;background:var(--navy)}
.estimate-ring{position:absolute;left:54px;top:52px;width:192px;height:192px;border:2px solid rgba(255,255,255,.35);border-radius:50%;display:flex;align-items:center;justify-content:center;text-align:center;color:var(--white);font-family:"Montserrat",Arial,sans-serif;font-weight:600;font-size:17px;line-height:25px}

/* features */
.feature{position:absolute;top:970px;width:260px;text-align:center;font-size:16px;line-height:25px;color:var(--text)}
.feature svg{display:block;margin:0 auto 14px}
.features-btn{left:508px;top:1148px;width:186px;height:40px;font-size:13px}

/* about */
.about-bg{left:0;top:1262px;width:601px;height:452px;background:var(--light)}
.about-photo{left:601px;top:1262px;width:599px;height:452px;background:linear-gradient(100deg,#dfe3e6 0%,#c7cdd3 40%,#5d7fb5 70%,#2f5aa0 100%)}
.about-title{left:75px;top:1330px;font-family:"Montserrat",Arial,sans-serif;font-weight:700;font-size:28px;color:var(--ink)}
.about-copy{left:75px;top:1385px;width:460px;font-size:13px;line-height:21px;color:var(--muted)}
.about-copy p+p{margin-top:14px}
.about-btn{left:75px;top:1603px;width:140px;height:38px;font-size:13px}

/* projects */
.section-title{left:0;width:1200px;text-align:center;font-family:"Montserrat",Arial,sans-serif;font-weight:700;font-size:29px;color:var(--ink)}
.arrow-btn{position:absolute;top:1776px;width:24px;height:24px;border:1.5px solid #9aa0a8;border-radius:50%}
.project{position:absolute;top:1863px;width:351px;text-align:center}
.project-img{width:351px;height:450px}
.project-name{margin-top:30px;font-family:"Montserrat",Arial,sans-serif;font-weight:600;font-size:16px;color:var(--ink)}
.project-name.active{color:#2a7fd4}
.project-rule{width:42px;height:2px;background:var(--green);margin:10px auto 12px;visibility:hidden}
.project-rule.active{visibility:visible}
.project-meta{font-size:12px;line-height:20px;color:var(--muted)}

/* testimonials */
.reviews{left:0;top:2544px;width:1200px;height:450px;background:var(--navy)}
.reviews-title{left:0;top:2606px;width:1200px;text-align:center;font-family:"Montserrat",Arial,sans-serif;font-weight:700;font-size:27px;color:var(--white)}
.quote{left:280px;top:2672px;width:640px;text-align:center;font-style:italic;font-size:17px;line-height:28px;color:#e7ebf3}
.quote-mark{color:#5f9be0;font-size:26px;font-style:normal}
.avatar{left:569px;top:2796px;width:62px;height:62px;border-radius:50%;background:linear-gradient(#f2d9b8,#d8b07a);border:3px solid var(--white)}
.reviewer{left:0;top:2874px;width:1200px;text-align:center;font-family:"Montserrat",Arial,sans-serif;font-weight:600;font-size:16px;color:var(--white)}
.stars{left:0;top:2898px;width:1200px;text-align:center;color:var(--green);font-size:13px;letter-spacing:2px}

/* services band */
.city{left:0;top:2994px;width:1200px;height:269px;background:linear-gradient(180deg,#3a3e45 0%,#2f3238 100%)}
.service-box{position:absolute;top:3066px;height:113px;border:1px solid var(--green);display:flex;align-items:center;gap:22px;padding-left:40px;background:rgba(30,33,38,.35)}
.service-title{font-family:"Montserrat",Arial,sans-serif;font-weight:600;font-size:17px;color:var(--white)}
.service-text{font-size:13px;line-height:19px;color:#cfd2d6;margin-top:4px;max-width:340px}

/* contact form */
.form-bg{left:0;top:3263px;width:1200px;height:501px;background:var(--charcoal)}
.form-title{left:0;top:3322px;width:1200px;text-align:center;font-family:"Montserrat",Arial,sans-serif;font-weight:700;font-size:29px;color:var(--white)}
.form-sub{left:0;top:3367px;width:1200px;text-align:center;font-size:13px;color:#a9adb3}
.field{position:absolute;background:var(--field);color:#aeb2b8;font-size:11px;letter-spacing:1px;padding:12px 20px;font-family:"Montserrat",Arial,sans-serif}
.call-line{left:0;top:3642px;width:1200px;text-align:center;font-family:"Montserrat",Arial,sans-serif;font-weight:600;font-size:16px;color:var(--white)}
.call-line span{color:var(--green)}
.hours{left:0;top:3672px;width:1200px;text-align:center;font-size:12px;color:#8d9197}
.form-btn{left:506px;top:3722px;width:188px;height:36px;font-size:13px}

/* footer */
.footer{left:0;top:3764px;width:1200px;height:90px;background:var(--footer)}
.copyright{left:150px;top:3800px;font-size:13px;color:#9a9ea4}
.social{left:768px;top:3799px;display:flex;gap:14px;align-items:center;color:#6e7278;font-size:12px}
.social i{display:block;width:14px;height:14px;border:1.5px solid #8a8e94;border-radius:2px}
.footer-cell{position:absolute;top:3764px;width:88px;height:90px;display:flex;align-items:center;justify-content:center}
</style>
</head>
<body>

<!-- hero -->
<div class="photo hero" role="img" aria-label="Photo of a frameless glass shower enclosure in a bright tiled bathroom"></div>
<div class="abs brand"><span class="brand-mark"></span><span class="brand-name">Brightvale</span></div>
<nav class="abs nav"><span class="active">Home</span><span>About</span><span>Services</span><span>Projects</span><span>Contact</span></nav>
<div class="abs nav-phone">Call (555) 014-2287</div>
<div class="btn btn-navy nav-quote">Request A Quote</div>
<h1 class="abs hero-title">Custom Designed &amp; Fabricated</h1>
<h2 class="abs hero-sub">Frameless Glass Showers Enclosures</h2>
<div class="btn btn-green hero-call">Call Now! (555) 014-2287</div>

<!-- service tabs -->
<div class="tab" style="left:0">
  <div class="tab-label">Custom Design</div>
  <div class="tab-img" role="img" aria-label="Photo of a glass shower with towel in a white bathroom" style="background:linear-gradient(90deg,#eef0f1,#c9ced2 60%,#9aa1a8)"></div>
</div>
<div class="tab tab-active" style="left:300px">
  <div class="tab-label">Fabrication</div>
  <div class="tab-img" role="img" aria-label="Photo of glass panels being fabricated" style="background:linear-gradient(135deg,#5a5f66,#2e3237)"></div>
  <div class="tab-overlay">Lorem ipsum dolor sit amet, consectetur adipiscing elit, sed do eiusmod tempor incididunt ut labore et dolore magna aliqua ut enim.<span class="tab-more">More</span></div>
</div>
<div class="tab" style="left:600px">
  <div class="tab-label">Installation</div>
  <div class="tab-img" role="img" aria-label="Photo of an installer fitting a glass shower door" style="background:linear-gradient(90deg,#d8dbde,#8fa2bd 55%,#3e69a8)"></div>
</div>
<div class="abs estimate"><div class="estimate-ring">Get An<br>Estimates<br>Today!</div></div>

<!-- features -->
<div class="feature" style="left:170px">
  <svg width="34" height="34" viewBox="0 0 34 34" fill="none" stroke="#2a4f94" stroke-width="2" stroke-linejoin="round"><rect x="3" y="15" width="6" height="15"/><path d="M9 16l7-11c2 0 3 1 3 3l-1 6h9c2 0 3 2 2 4l-3 10c-1 2-2 2-4 2H9"/></svg>
  More then 10 Years of experience
</div>
<div class="feature" style="left:470px">
  <svg width="34" height="34" viewBox="0 0 34 34" fill="none" stroke="#2a4f94" stroke-width="2"><circle cx="17" cy="11" r="7"/><path d="M5 32c0-7 5-12 12-12s12 5 12 12"/></svg>
  We Deliver Best Glass Products and Services in Texas
</div>
<div class="feature" style="left:770px">
  <svg width="34" height="34" viewBox="0 0 34 34" fill="none" stroke="#2a4f94" stroke-width="2"><path d="M17 2v30M24 9c-1-3-4-4-7-4s-7 2-7 5 3 5 7 6 8 3 8 7-3 5-8 5-7-2-8-5"/></svg>
  Completed on time and within budget
</div>
<div class="btn btn-green features-btn">Contact Us Today!</div>

<!-- about -->
<div class="abs about-bg"></div>
<div class="photo about-photo" role="img" aria-label="Photo of a worker in a hard hat installing a glass shower panel"></div>
<h2 class="abs about-title">We Love What We Do!</h2>
<div class="abs about-copy">
  <p>Brightvale Bath Panels &amp; Glass LLC. is committed to excellence in every aspect of our business. We hold a standard of integrity bound by fairness, honesty, and personal responsibility.</p>
  <p>Our distinction is the quality of service and attention to detail we bring to each project. Above all, we listen to our clients input to provide several design options available from designer glass to hardware.</p>
</div>
<div class="btn btn-green about-btn">About Us</div>

<!-- projects -->
<h2 class="abs section-title" style="top:1770px">Completed Projects</h2>
<span class="arrow-btn" style="left:200px"></span>
<span class="arrow-btn" style="left:976px;border-color:#2a4f94"></span>
<div class="project" style="left:39px">
  <div class="project-img" role="img" aria-label="Photo of a sliding glass shower with white tray" style="background:linear-gradient(180deg,#b7b8b8,#8d8e8e 70%,#e6e6e6)"></div>
  <div class="project-name active">Header Less Sliding Door</div>
  <div class="project-rule active"></div>
  <div class="project-meta">Glass: 1/2" Glass Only<br>Location: NY</div>
</div>
<div class="project" style="left:424px">
  <div class="project-img" role="img" aria-label="Photo of an inline glass shower on a wooden floor" style="background:linear-gradient(180deg,#6f7275,#4b4e51 60%,#7a5c43)"></div>
  <div class="project-name">Inline Shower Doors</div>
  <div class="project-rule"></div>
  <div class="project-meta">Glass: Heavy Duty Tempered Glass<br>Hardware: Solid Brass<br>Location: NY</div>
</div>
<div class="project" style="left:812px">
  <div class="project-img" role="img" aria-label="Photo of a curved corner glass shower" style="background:linear-gradient(180deg,#9ea0a2,#7d7f81 70%,#c9c9c9)"></div>
  <div class="project-name">Corner Showers and Door</div>
  <div class="project-rule"></div>
  <div class="project-meta">Glass: 1/2" Glass Only<br>Location: TX</div>
</div>

<!-- reviews -->
<div class="abs reviews"></div>
<h2 class="abs reviews-title">Happy Customers</h2>
<p class="abs quote"><span class="quote-mark">&ldquo;</span> We decided on a glass guardrail for our decking, and the results are fantastic. We will be considering a Brightvale Bath Panels and Glass as we move our project forward. <span class="quote-mark">&rdquo;</span></p>
<svg class="abs" style="left:498px;top:2818px" width="12" height="14" viewBox="0 0 12 14" fill="none" stroke="#aebde0" stroke-width="1.6"><path d="M8 2L3 7l5 5"/></svg>
<svg class="abs" style="left:690px;top:2818px" width="12" height="14" viewBox="0 0 12 14" fill="none" stroke="#aebde0" stroke-width="1.6"><path d="M4 2l5 5-5 5"/></svg>
<div class="abs avatar" role="img" aria-label="Customer portrait"></div>
<div class="abs reviewer">Clara Wendt</div>
<div class="abs stars">★★★★★</div>

<!-- services band -->
<div class="photo city" role="img" aria-label="Dark photo of a city skyline"></div>
<div class="service-box" style="left:77px;width:504px">
  <svg width="56" height="56" viewBox="0 0 56 56" fill="var(--green)"><path d="M12 24a16 16 0 0 1 32 0h4v5H8v-5z"/><rect x="14" y="33" width="28" height="4"/><path d="M8 54c0-10 8-14 20-14s20 4 20 14z"/></svg>
  <div><div class="service-title">Repair &amp; Installation</div><div class="service-text">Professional repair and installation by our expert team.</div></div>
</div>
<div class="service-box" style="left:617px;width:506px">
  <svg width="56" height="56" viewBox="0 0 56 56" fill="var(--green)"><rect x="22" y="-2" width="12" height="60" transform="rotate(45 28 28)"/><rect x="22" y="-2" width="12" height="60" transform="rotate(-45 28 28)"/></svg>
  <div><div class="service-title">Any Size &amp; Shape</div><div class="service-text">Custom size shower enclosure for any bath-room project.</div></div>
</div>

<!-- quote form -->
<div class="abs form-bg"></div>
<h2 class="abs form-title">Get a Free Quote Today!</h2>
<p class="abs form-sub">We have been transforming the ideas and visions into award-winning projects.</p>
<div class="field" style="left:149px;top:3415px;width:308px;height:36px">ENTER YOUR NAME</div>
<div class="field" style="left:478px;top:3415px;width:308px;height:36px">EMAIL</div>
<div class="field" style="left:807px;top:3415px;width:241px;height:36px">PHONE</div>
<div class="field" style="left:149px;top:3472px;width:899px;height:138px">MESSAGE ...</div>
<div class="abs call-line">You can also call us @ <span>(555) 014-2287</span></div>
<div class="abs hours">Mon to Fri : 09:00 - 5:00</div>
<div class="btn btn-navy form-btn">Request A Quote</div>

<!-- footer -->
<div class="abs footer"></div>
<div class="abs copyright">© 2019 Brightvale Bath Panels &amp; Glass LLC</div>
<div class="abs social"><i></i>/<i></i>/<i></i></div>
<div class="footer-cell" style="left:934px;background:#2b2e35">
  <svg width="14" height="18" viewBox="0 0 14 18" fill="none" stroke="#8a8e94" stroke-width="1.6"><path d="M7 17s6-6 6-10A6 6 0 0 0 1 7c0 4 6 10 6 10z"/><circle cx="7" cy="7" r="2"/></svg>
</div>
<div class="footer-cell" style="left:1064px">
  <svg width="14" height="10" viewBox="0 0 14 10" fill="none" stroke="#8a8e94" stroke-width="1.6"><path d="M2 8l5-5 5 5"/></svg>
</div>

</body>
</html>
```